"Rodrigo Velvet" Business Card

Friends

My name is "Rodrigo Velvet" and I need your help! I need a new business card for my personal use.

As background, "Rodrigo Velvet" is actually an alias that I use when I meet women. Please use your creative skills to create an amazing business card for me to use!

In addition to including my name and contact details (see the "Must Have" section), you may wish to add a catchphrase or a title if you think it would help me :)

For background, please see:

http://www.dailyripplenews.com/2013/07/23/marcus-pell-rodrigo-velvet_n_8152704.html

Looking forward to seeing what you can do for me.

Hugs and kisses,

Rodrigo Velvet [courtesy of ArtQuarry]

Target Market(s)

Adult women in New York City...or anywhere really.

Industry/Entity Type

Business

Requirements
Must have
• Please include the following details:

Rodrigo Velvet
P: +1-555-4VELVET
E: secrets@rodrigovelvet.example
Nice to have
• You might include a catchphrase, like "Velvet is my surname But you can call me Mr Hardbody".

Or perhaps a title, like "Rodrigo Velvet, Head of Sexy Times".

You're creative...I will leave the details to you my friends.
Should not have
• Any references to my actual name...because then, what's the point in using an alias?

```html
<!DOCTYPE html>
<html lang="en">
<head>
<meta charset="utf-8">
<title>Rodrigo Velvet — Business Card</title>
<link rel="stylesheet" href="https://fonts.googleapis.com/css2?family=Open+Sans:ital,wght@0,300;0,400;0,800;1,300;1,400&display=swap">
<style>
  :root {
    --card-black: #000000;
    --gold: #e2b234;
    --gold-deep: #d4a12a;
    --label-white: #ffffff;
  }
  html, body {
    margin: 0;
    padding: 0;
    width: 1200px;
    height: 675px;
    overflow: hidden;
    background: var(--card-black);
  }
  .business-card {
    position: relative;
    width: 1200px;
    height: 675px;
    background: var(--card-black);
    font-family: "Open Sans", Arial, sans-serif;
    overflow: hidden;
  }
  .brand-name {
    position: absolute;
    left: 0;
    width: 1200px;
    top: 158px;
    margin: 0;
    text-align: center;
    font-weight: 800;
    font-style: normal;
    font-size: 84px;
    line-height: 1;
    letter-spacing: 1px;
    color: var(--gold);
    padding-left: 12px;
    box-sizing: border-box;
  }
  .job-title {
    position: absolute;
    left: 0;
    width: 1200px;
    top: 244px;
    margin: 0;
    text-align: center;
    padding-left: 12px;
    box-sizing: border-box;
    font-style: italic;
    font-weight: 400;
    font-size: 37px;
    line-height: 1;
    color: var(--gold-deep);
  }
  .contact-list {
    position: absolute;
    left: 352px;
    top: 409px;
    margin: 0;
    padding: 0;
    list-style: none;
    font-style: italic;
    font-weight: 300;
    font-size: 31px;
    line-height: 37px;
  }
  .contact-label { color: var(--label-white); }
  .contact-value { color: var(--gold); }
  .tagline {
    position: absolute;
    left: 0;
    width: 1200px;
    top: 613px;
    margin: 0;
    text-align: center;
    padding-left: 12px;
    box-sizing: border-box;
    font-style: italic;
    font-weight: 400;
    font-size: 39px;
    line-height: 1;
    color: var(--gold-deep);
  }
</style>
</head>
<body>
  <main class="business-card">
    <h1 class="brand-name">RODRIGO VELVET</h1>
    <p class="job-title">HEAD OF SEXY TIMES</p>
    <ul class="contact-list">
      <li><span class="contact-label">email: </span><span class="contact-value">secrets@rodrigovelvet.example</span></li>
      <li><span class="contact-label">Phone: </span><span class="contact-value">+1-555-4VELVET</span></li>
    </ul>
    <p class="tagline">Rodrigo is my name, but you can call me Mr Hardbody</p>
  </main>
</body>
</html>
```